【依頼の目的/概要】
電子書籍(plumet)の表紙デザインをお願いします。

【画像サイズ】
表紙ファイルの理想的な寸法は2,560×1,600ピクセルです。

【タイトル】
あの窓辺にまた灯りがともる静かな暮らしの場を一から育てるための手引き

サブキャッチ
~住む人の歩みを一緒に編み直す語らい中心の新しい手法~

【著者】
株式会社MRTOV
代表取締役 江坂 なつえ

【本の内容】
誰もが迎える老いのステージを「自分の人生まんざらでもなかったなぁ」と思っていただける新手法ナラティブアプローチの方法を介護哲学と共に解説しています。

*本文を参考資料として添付します。

【デザイン要望】
特にイメージにこだわりはありませんので、自由な発想でのデザインご応募を楽しみにしています。
*次点、次次点の方への参加報酬を設定いたしました。
*その他、必要な情報がありましたらお問い合わせください。

暖かいイメージが伝わってきます。
一番人気でした。

この度は力作を多数ご提案いただき、有難うございました。
初めてワクトリアを利用させていただいたのですが、たくさんの洗練されたご提案があったこと、はるかに自分の予想を上回りました。
これからも、利用させていただきたいと思いますので、よろしくお願いいたします。

```html
<!DOCTYPE html>
<html lang="ja">
<head>
<meta charset="utf-8">
<title>あの窓辺にまた灯りがともる静かな暮らしの場を一から育てるための手引き</title>
<link rel="stylesheet" href="https://fonts.googleapis.com/css2?family=Noto+Serif+JP:wght@500;700;900&display=swap">
<style>
  :root {
    --paper: #ffffff;
    --ink: #3b2c24;
    --title-black: #1c1512;
    --accent-red: #c8161d;
    --photo-wall: #e9e4da;
    --photo-window: #d7dde0;
    --photo-skin: #d8b79c;
    --photo-cloth: #8c97a6;
    --photo-table: #b9a48b;
    --illust-warm: #e7b7a9;
    --illust-cool: #b9c3cf;
  }
  html, body {
    margin: 0;
    padding: 0;
    overflow: hidden;
    background: var(--paper);
  }
  .cover {
    position: relative;
    width: 749px;
    height: 1200px;
    overflow: hidden;
    background: var(--paper);
    font-family: "Noto Serif JP", serif;
  }
  .cover-photo {
    position: absolute;
    left: 0;
    top: 560px;
    width: 749px;
    height: 640px;
    background:
      linear-gradient(to bottom, var(--paper) 0%, rgba(255,255,255,0) 22%),
      radial-gradient(ellipse 30% 22% at 22% 72%, var(--photo-skin) 0%, rgba(216,183,156,0) 100%),
      radial-gradient(ellipse 26% 20% at 55% 78%, var(--photo-skin) 0%, rgba(216,183,156,0) 100%),
      radial-gradient(ellipse 24% 20% at 82% 74%, var(--photo-cloth) 0%, rgba(140,151,166,0) 100%),
      linear-gradient(to bottom, var(--photo-wall) 0%, var(--photo-window) 45%, var(--photo-table) 100%);
  }
  .care-illustration {
    position: absolute;
    left: 580px;
    top: 610px;
    width: 150px;
    height: 190px;
    background: radial-gradient(ellipse at 50% 50%, var(--illust-warm) 0%, var(--illust-cool) 55%, rgba(185,195,207,0) 100%);
    opacity: 0.7;
  }
  .vcol {
    position: absolute;
    writing-mode: vertical-rl;
    text-orientation: upright;
    white-space: nowrap;
    line-height: 1;
    margin: 0;
  }
  .lead-small {
    left: 662px;
    top: 28px;
    font-size: 33px;
    font-weight: 500;
    color: var(--ink);
  }
  .lead-red {
    left: 608px;
    top: 28px;
    font-size: 33px;
    font-weight: 700;
    color: var(--accent-red);
  }
  .title-main {
    left: 420px;
    top: 24px;
    font-size: 118px;
    font-weight: 900;
    color: var(--accent-red);
  }
  .title-second {
    left: 284px;
    top: 160px;
    font-size: 110px;
    font-weight: 900;
    color: var(--title-black);
  }
  .subtitle-dark {
    left: 222px;
    top: 70px;
    font-size: 37px;
    font-weight: 700;
    color: var(--ink);
  }
  .subtitle-red {
    left: 158px;
    top: 70px;
    font-size: 46px;
    font-weight: 900;
    color: var(--accent-red);
  }
  .author-company {
    left: 104px;
    top: 250px;
    font-size: 16px;
    font-weight: 500;
    color: var(--ink);
  }
  .author-role {
    left: 82px;
    top: 250px;
    font-size: 16px;
    font-weight: 500;
    color: var(--ink);
  }
  .author-name {
    left: 32px;
    top: 370px;
    font-size: 40px;
    font-weight: 700;
    color: var(--title-black);
    letter-spacing: 0.05em;
  }
</style>
</head>
<body>
  <main class="cover">
    <div class="cover-photo" role="img" aria-label="明るい共用スペースで笑顔で拍手する入居者とスタッフの写真"></div>
    <div class="care-illustration" role="img" aria-label="車椅子の高齢者と介助する職員のイラスト"></div>

    <p class="vcol lead-small">あの窓辺にまた灯りが</p>
    <p class="vcol lead-red">ともる静かな暮らしの場を</p>
    <h1 class="vcol title-main">一から育てる</h1>
    <p class="vcol title-second">ための手引き</p>

    <p class="vcol subtitle-dark">住む人の歩みを一緒に編み直す</p>
    <p class="vcol subtitle-red">語らい中心の新しい手法</p>

    <p class="vcol author-company">株式会社ＭＲＴＯＶ</p>
    <p class="vcol author-role">代表取締役</p>
    <p class="vcol author-name">江坂 なつえ</p>
  </main>
</body>
</html>
```